TR Advisory Business Cards - High End AV / Low Voltage Company

We are low voltage AV company that specializes in high end clients on the residential side and larger businesses on the commercial side. We want something modern, tech looking but also something that is extremely professional looking. We have uploaded our logos and postcards we already have in the field. Along with a picture of one of our wrapped vans. Our website is at www.trvadvisory.example and our primary colors are the orange, green, grey and blue all military color finishes.

We are interesting in the slogans "Pairing You with the Right Technology" or "Leading the Lowcountry in Tech"

Target Market(s)

We focus on 70% Commercial and 30% Residential Customers

Industry/Entity Type

Low Voltage, AV Company

Contact Information for Business Card

Name - Dorian Fairweather, Title - Owner, Office Phone - 555-714-3096, Mobile Phone - 555-802-4173, E-Mail - d@trvadvisory.example, Website: www.trvadvisory.example

Font styles to use
Sans Serif

Requirements
Must have
• Must have Name, Title, Work Phone & Mobile, Website and Logo.
Nice to have
• We want something that will impress our higher end clients with a great logo
Should not have
• Too traditional or plain.

```html
<!DOCTYPE html>
<html lang="en">
<head>
<meta charset="utf-8">
<title>TR Advisory Business Cards</title>
<link rel="stylesheet" href="https://fonts.googleapis.com/css2?family=Arimo:wght@400;700&display=swap">
<style>
  :root {
    --bg: #9a9a9a;
    --paper: #f6f6f5;
    --brand-orange: #e06033;
    --ink: #2b2b2b;
    --muted: #6a6a6a;
    --rule: #5a5a5a;
    --white: #ffffff;
  }
  * { margin: 0; padding: 0; box-sizing: border-box; }
  html, body {
    width: 1200px; height: 1050px; overflow: hidden;
    background: var(--bg);
    font-family: "Arimo", Arial, sans-serif;
  }
  .canvas { position: relative; width: 1200px; height: 1050px; }

  .card {
    position: absolute;
    border-radius: 22px;
    box-shadow: 0 6px 14px rgba(0,0,0,0.22);
  }

  /* Front: portrait white card */
  .card-front {
    left: 90px; top: 205px; width: 370px; height: 640px;
    background: var(--paper);
  }
  .front-mark {
    position: absolute; left: 40px; top: 52px;
    display: flex; align-items: center; gap: 12px;
  }
  .mark-circle {
    width: 46px; height: 46px; border-radius: 50%;
    border: 4px solid var(--brand-orange);
  }
  .mark-name {
    font-weight: 700; font-size: 26px; color: var(--brand-orange);
    letter-spacing: 0.5px;
  }
  .identity { position: absolute; left: 40px; top: 390px; }
  .person-name {
    font-weight: 700; font-size: 25px; color: var(--brand-orange);
  }
  .person-title {
    margin-top: 6px; font-size: 16px; color: var(--muted);
  }
  .divider {
    position: absolute; left: 40px; top: 468px;
    width: 46px; height: 2px; background: var(--rule);
  }
  .contacts {
    position: absolute; left: 40px; top: 494px;
    list-style: none;
  }
  .contacts li {
    display: flex; align-items: center; gap: 10px;
    font-size: 16px; color: var(--ink); line-height: 26px;
  }
  .contacts svg { width: 14px; height: 14px; flex: none; }

  /* Back: landscape orange card */
  .card-back {
    left: 510px; top: 342px; width: 620px; height: 366px;
    background: var(--brand-orange);
    display: flex; align-items: center; justify-content: center;
  }
  .back-mark { display: flex; align-items: center; gap: 20px; }
  .back-mark .mark-circle {
    width: 82px; height: 82px; border: 7px solid var(--white);
  }
  .back-mark .mark-name {
    color: var(--white); font-size: 52px; letter-spacing: 1px;
  }
</style>
</head>
<body>
<main class="canvas">

  <section class="card card-front" aria-label="Business card front">
    <div class="front-mark">
      <span class="mark-circle"></span>
      <span class="mark-name">TR Advisory</span>
    </div>

    <div class="identity">
      <p class="person-name">Dorian Fairweather</p>
      <p class="person-title">Owner</p>
    </div>
    <span class="divider"></span>

    <ul class="contacts">
      <li>
        <svg viewBox="0 0 16 16" aria-hidden="true"><path d="M3 1.5l3 .5 1 3.5-2 1.2a9 9 0 0 0 4.3 4.3l1.2-2 3.5 1 .5 3c-.3.8-1.2 1.5-2 1.5C7 14.5 1.5 9 1.5 3.5c0-.8.7-1.7 1.5-2z" fill="#e06033"/></svg>
        555-714-3096
      </li>
      <li>
        <svg viewBox="0 0 16 16" aria-hidden="true"><rect x="4" y="1" width="8" height="14" rx="1.5" fill="none" stroke="#e06033" stroke-width="1.6"/><circle cx="8" cy="12.5" r="0.9" fill="#e06033"/></svg>
        555-802-4173
      </li>
      <li>
        <svg viewBox="0 0 16 16" aria-hidden="true"><rect x="1.5" y="3.5" width="13" height="9" rx="1" fill="#e06033"/><path d="M2 4.5l6 4.5 6-4.5" fill="none" stroke="#ffffff" stroke-width="1.2"/></svg>
        d@trvadvisory.example
      </li>
      <li>
        <svg viewBox="0 0 16 16" aria-hidden="true"><circle cx="8" cy="8" r="6.5" fill="#e06033"/><path d="M1.5 8h13M8 1.5c2.5 2 2.5 11 0 13M8 1.5c-2.5 2-2.5 11 0 13" fill="none" stroke="#ffffff" stroke-width="0.9"/></svg>
        www.trvadvisory.example
      </li>
    </ul>
  </section>

  <section class="card card-back" aria-label="Business card back">
    <div class="back-mark">
      <span class="mark-circle"></span>
      <span class="mark-name">TR Advisory</span>
    </div>
  </section>

</main>
</body>
</html>
```